Letterhead for a Natural Hair Run

We need a letterhead design with the logo uploaded entitled 'Zephlyra Dash'. This run is a natural 5K run seeking to promote the acceptance of natural beauty in every aspect of society encompassing one's ethnic roots and its connection to a healthy lifetstyle. We would like to see designs coordinating with our logo. The design should be fun and exciting!

Industry/Entity Type

Hair

Font styles to use
Serif
Sans Serif

Requirements
Must have
• Please included this information on the letter head:
• P.O. Box K7214
• Nassau, Bahamas
• Phone: (242) 618-2907
• Email: goskyward417@mailvista.net

```html
<!DOCTYPE html>
<html lang="en">
<head>
<meta charset="utf-8">
<title>Zephlyra Dash Stationery</title>
<link href="https://fonts.googleapis.com/css2?family=Lato:wght@400;700&display=swap" rel="stylesheet">
<style>
  :root {
    --backdrop: #141414;
    --paper: #ffffff;
    --brand-blue: #00b4d4;
    --flap-text: #2ec6e0;
    --ink: #3a3a3a;
    --ink-soft: #555555;
    --logo-ink: #1c1c1c;
  }
  * { margin: 0; padding: 0; box-sizing: border-box; }
  html, body { width: 1200px; height: 1001px; overflow: hidden; background: var(--backdrop); }
  body { position: relative; font-family: 'Lato', Arial, sans-serif; color: var(--ink); }

  .brand-name { font-family: 'Lato', Arial, sans-serif; font-weight: 700; color: var(--logo-ink); white-space: nowrap; display: flex; align-items: center; gap: 5px; }
  .brand-dot { display: inline-block; border-radius: 50%; background: var(--brand-blue); }

  /* Letterhead */
  .letterhead { position: absolute; left: 120px; top: 141px; width: 424px; height: 635px; background: var(--paper); overflow: hidden; }
  .letterhead .brand-name { position: absolute; left: 30px; top: 22px; font-size: 13px; }
  .letterhead .brand-dot { width: 9px; height: 9px; }
  .letterhead .header-rule { position: absolute; left: 0; top: 55px; width: 100%; height: 2px; background: var(--brand-blue); }
  .header-contact { position: absolute; right: 22px; top: 18px; text-align: right; font-size: 5.5px; line-height: 10.5px; color: var(--ink); }
  .header-contact .row { display: flex; justify-content: flex-end; align-items: center; gap: 3px; }
  .header-contact svg { width: 5px; height: 5px; fill: var(--brand-blue); }

  .recipient { position: absolute; left: 34px; top: 83px; font-size: 9px; line-height: 14.8px; color: var(--ink); }
  .recipient .name { font-weight: 700; }
  .salutation { position: absolute; left: 34px; top: 181px; font-size: 10px; font-weight: 700; color: var(--ink); }
  .letter-body { position: absolute; left: 33px; top: 200px; width: 358px; font-size: 5.9px; line-height: 16.2px; color: var(--ink-soft); text-align: justify; }
  .letter-body p + p { margin-top: 8px; }
  .letter-body p:nth-child(3) { margin-top: 12px; }

  .closing { position: absolute; left: 34px; top: 483px; font-size: 8.5px; color: var(--ink); }
  .closing .sign-line { margin-top: 6px; line-height: 16px; }
  .faithfully { position: absolute; left: 329px; top: 483px; font-size: 8.5px; color: var(--ink); }

  .corner-wave { position: absolute; left: 0; top: 0; width: 424px; height: 635px; }
  .footer-address { position: absolute; right: 14px; top: 585px; font-size: 5.8px; line-height: 8px; color: var(--paper); text-align: right; }
  .footer-address .row { display: flex; justify-content: flex-end; align-items: center; gap: 3px; }
  .footer-address svg { width: 5px; height: 6px; fill: var(--paper); }

  /* Business card */
  .business-card { position: absolute; left: 608px; top: 190px; width: 489px; height: 245px; background: var(--paper); }
  .business-card .brand-name { position: absolute; left: 24px; top: 60px; font-size: 22px; }
  .business-card .brand-dot { width: 14px; height: 14px; }
  .card-contact { position: absolute; left: 26px; top: 146px; font-size: 6.6px; line-height: 12.8px; color: var(--ink); }
  .card-contact .row { display: flex; align-items: center; gap: 7px; }
  .card-contact svg { width: 5.5px; height: 6px; fill: var(--brand-blue); }
  .card-rule { position: absolute; left: 0; top: 205px; width: 100%; height: 2.5px; background: var(--brand-blue); }

  /* Envelope */
  .envelope { position: absolute; left: 609px; top: 482px; width: 500px; height: 250px; background: var(--paper); }
  .envelope-flap { position: absolute; left: 0; top: 0; width: 500px; height: 66px; }
  .flap-name { position: absolute; left: 0; top: 20px; width: 100%; text-align: center; font-size: 26px; font-weight: 400; letter-spacing: 1px; color: var(--flap-text); }
</style>
</head>
<body>

<section class="letterhead">
  <div class="brand-name"><span class="brand-dot"></span>Zephlyra Dash</div>
  <div class="header-contact">
    <div class="row">(242) 618-2907 <svg viewBox="0 0 10 10"><path d="M2 1 L4 1 L5 3.5 L3.7 4.5 Q4.5 6 6 6.5 L7 5.2 L9.5 6.2 L9.5 8.5 Q9 9.5 7.5 9 Q2 7.5 1 2.5 Q1 1.2 2 1Z"/></svg></div>
    <div class="row">goskyward417@mailvista.net <svg viewBox="0 0 10 10"><path d="M0.5 2 H9.5 V8 H0.5Z"/></svg></div>
  </div>
  <div class="header-rule"></div>

  <div class="recipient">
    <div class="name">Marcus Ellery</div>
    <div>Owner</div>
    <div>Company Name</div>
    <div>Address Line1, Address Line2</div>
    <div>Country -123456</div>
  </div>

  <div class="salutation">Dear Marcus Ellery</div>

  <div class="letter-body">
    <p>Lorem ipsum dolor sit amet, consectetur adipiscing elit, sed do eiusmod tempor incididunt ut labore et dolore magna aliqua. Ut enim ad minim veniam, quis nostrud exercitation ullamco laboris nisi ut aliquip ex ea commodo consequat. Duis aute irure dolor in reprehenderit in voluptate velit esse cillum dolore eu fugiat nulla pariatur. Excepteur sint occaecat cupidatat non proident, sunt in culpa qui officia deserunt mollit anim id est laborum.</p>
    <p>Lorem ipsum dolor sit amet, consectetur adipiscing elit, sed do eiusmod tempor incididunt ut labore et dolore magna aliqua. Ut enim ad minim veniam, quis nostrud exercitation ullamco laboris nisi ut aliquip ex ea commodo consequat. Duis aute irure dolor in reprehenderit in voluptate velit esse cillum dolore</p>
    <p>Lorem ipsum dolor sit amet, consectetur adipiscing elit, sed do eiusmod tempor incididunt ut labore et dolore magna aliqua. Ut enim ad minim veniam, quis nostrud exercitation ullamco laboris nisi ut aliquip ex ea commodo consequat. Duis aute irure dolor in reprehenderit in voluptate velit esse cillum dolore eu fugiat nulla pariatur. Excepteur sint occaecat cupidatat non proident, sunt in culpa qui officia deserunt mollit anim id est laborum.</p>
  </div>

  <div class="closing">
    <div>Sincerely,</div>
    <div class="sign-line">[ your Name ]</div>
    <div>[ Title ]</div>
  </div>
  <div class="faithfully">Your Faithfully</div>

  <svg class="corner-wave" viewBox="0 0 424 635" aria-hidden="true">
    <path d="M424 422 C405 540 330 605 234 635 L424 635 Z" fill="var(--brand-blue)"/>
  </svg>
  <div class="footer-address">
    <div class="row">P.O. Box K7214 <svg viewBox="0 0 10 12"><path d="M5 0.5 A4 4 0 0 1 9 4.5 C9 7.5 5 11.5 5 11.5 C5 11.5 1 7.5 1 4.5 A4 4 0 0 1 5 0.5Z M5 3 A1.5 1.5 0 1 0 5 6 A1.5 1.5 0 1 0 5 3Z" fill-rule="evenodd"/></svg></div>
    <div class="row" style="padding-right:8px">Nassau, Bahamas</div>
  </div>
</section>

<section class="business-card">
  <div class="brand-name"><span class="brand-dot"></span>Zephlyra Dash</div>
  <div class="card-contact">
    <div class="row"><svg viewBox="0 0 10 10"><path d="M2 1 L4 1 L5 3.5 L3.7 4.5 Q4.5 6 6 6.5 L7 5.2 L9.5 6.2 L9.5 8.5 Q9 9.5 7.5 9 Q2 7.5 1 2.5 Q1 1.2 2 1Z"/></svg>(242) 618-2907</div>
    <div class="row"><svg viewBox="0 0 10 10"><path d="M0.5 2 H9.5 V8 H0.5Z"/></svg>goskyward417@mailvista.net</div>
    <div class="row"><svg viewBox="0 0 10 12"><path d="M5 0.5 A4 4 0 0 1 9 4.5 C9 7.5 5 11.5 5 11.5 C5 11.5 1 7.5 1 4.5 A4 4 0 0 1 5 0.5Z M5 3 A1.5 1.5 0 1 0 5 6 A1.5 1.5 0 1 0 5 3Z" fill-rule="evenodd"/></svg>P.O. Box K7214 Nassau, Bahamas</div>
  </div>
  <div class="card-rule"></div>
</section>

<section class="envelope">
  <svg class="envelope-flap" viewBox="0 0 500 66" aria-hidden="true">
    <path d="M0 0 H500 L481 66 H21 Z" fill="var(--brand-blue)"/>
  </svg>
  <div class="flap-name">Zephlyra Dash</div>
</section>

</body>
</html>
```